Business Card Design

We are a family run drainage & groundworks company that specialise in treatment plant installation. We work for commercial & domestic property's, we have specialised knowledge & equipment for CCTV surveys, jetting blockages & repairing all types of drainage systems.

Industry/Entity Type

Business

Contact Information for Business Card

14 Marlpit Workshops
Belcombe Mill Lane
Harnwick
Hampshire
SP4 7TN
Tel: 01632 960418
Fax: 01632 960752
Mobile: 07700 900318
enquiries@kestrelwd.co.uk
www.kestrelwastedrainage.co.uk

Requirements
Must have
• logo, address, the right colour green.
I need the cards to also have individuals names:

Tom lydgate
Neil Carrow
Helen Lydgate
Di Pemberton

And also some with just the name & address on :)

```html
<!DOCTYPE html>
<html lang="en">
<head>
<meta charset="utf-8">
<title>Kestrel Waste &amp; Drainage – Business Card</title>
<link rel="stylesheet" href="https://fonts.googleapis.com/css2?family=Source+Sans+3:wght@400;700&display=swap">
<style>
  :root {
    --brand-green: #2b9a45;
    --ink: #3a3a3a;
    --label-grey: #6b6b6b;
    --card-white: #ffffff;
    --edge-grey: #d4d4d4;
  }
  html, body {
    margin: 0;
    padding: 0;
    width: 1200px;
    height: 780px;
    overflow: hidden;
    background: var(--card-white);
  }
  .business-card {
    position: relative;
    width: 1200px;
    height: 780px;
    background: var(--card-white);
    border-top: 3px solid var(--edge-grey);
    border-bottom: 3px solid var(--edge-grey);
    box-sizing: border-box;
    font-family: "Source Sans 3", Arial, sans-serif;
    color: var(--ink);
  }
  .person-name {
    position: absolute;
    left: 658px;
    top: 60px;
    margin: 0;
    font-size: 54px;
    font-weight: 700;
    letter-spacing: 0.5px;
    color: var(--brand-green);
    text-transform: uppercase;
  }
  .contact-list {
    position: absolute;
    left: 660px;
    top: 212px;
    margin: 0;
    padding: 0;
    list-style: none;
  }
  .contact-item {
    display: flex;
    align-items: center;
    height: 50px;
    font-size: 30px;
  }
  .contact-label {
    width: 36px;
    font-size: 20px;
    color: var(--label-grey);
  }
  .contact-bullet {
    width: 8px;
    height: 8px;
    background: var(--brand-green);
    margin-right: 28px;
  }
  .postal-address {
    position: absolute;
    left: 656px;
    top: 506px;
    margin: 0;
    font-style: normal;
    font-size: 30px;
    line-height: 42px;
  }
  .website {
    position: absolute;
    left: 656px;
    top: 660px;
    margin: 0;
    font-size: 30px;
  }
  .company-mark {
    position: absolute;
    left: 76px;
    top: 466px;
    width: 240px;
    text-align: center;
  }
  .company-square {
    display: block;
    width: 170px;
    height: 170px;
    margin: 0 auto 16px;
    background: var(--brand-green);
  }
  .company-name {
    margin: 0;
    font-size: 23px;
    font-weight: 400;
    line-height: 29px;
    letter-spacing: 2.5px;
    text-transform: uppercase;
    color: var(--ink);
  }
</style>
</head>
<body>
  <div class="business-card">
    <h1 class="person-name">Tom Lydgate</h1>

    <ul class="contact-list">
      <li class="contact-item"><span class="contact-label">T</span><span class="contact-bullet"></span>01632 960418</li>
      <li class="contact-item"><span class="contact-label">F</span><span class="contact-bullet"></span>01632 960752</li>
      <li class="contact-item"><span class="contact-label">M</span><span class="contact-bullet"></span>07700 900318</li>
      <li class="contact-item"><span class="contact-label">E</span><span class="contact-bullet"></span>enquiries@kestrelwd.co.uk</li>
    </ul>

    <address class="postal-address">
      14 Marlpit Workshops<br>
      Belcombe Mill Lane Harnwick<br>
      Hampshire SP4 7TN
    </address>

    <p class="website">www.kestrelwastedrainage.co.uk</p>

    <div class="company-mark">
      <span class="company-square"></span>
      <p class="company-name">Kestrel Waste<br>&amp; Drainage</p>
    </div>
  </div>
</body>
</html>
```